Business Card Design

BBQ Concessions and Event Catering
Hi! My name is Walt I am looking for a biz card design for my BBQ company:
We specialize in ribs, brisket, pulled pork, chicken
Mainly Pork Product
Colors: Dark colors, Red, Black
Flames optional
This is a mobile trailer that moves to the party!
Copper Gate is a song by Lonnie Tasker which influenced the name of my company. So I Love Blues and BBQ!
We also cater at music venues, parties, receptions etc. Anyone who needs good BBQ comes to us.

Looking forward to your designs.

Industry/Entity Type

Business

Contact Information for Business Card

Copper Gate BBQ, Walt Barcombe Owner, 2218 Dunmore Ave. Millbrook, In. 46391

```html
<!DOCTYPE html>
<html lang="en">
<head>
<meta charset="utf-8">
<title>Copper Gate BBQ – Business Card</title>
<link rel="stylesheet" href="https://fonts.googleapis.com/css2?family=Archivo+Black&family=Arimo:wght@400&display=swap">
<style>
  :root {
    --backdrop: #d9d4cc;
    --card: #ffffff;
    --ink: #111111;
    --accent: #e31b23;
    --shadow: rgba(0, 0, 0, 0.18);
  }
  html, body {
    margin: 0;
    padding: 0;
    width: 1200px;
    height: 870px;
    overflow: hidden;
    background: var(--backdrop);
  }
  .canvas {
    position: relative;
    width: 1200px;
    height: 870px;
    display: flex;
    align-items: center;
    justify-content: center;
  }
  .business-card {
    position: relative;
    width: 446px;
    height: 780px;
    background: var(--card);
    box-shadow: 0 6px 22px var(--shadow);
    overflow: hidden;
    text-align: center;
    color: var(--ink);
  }
  .brand-name {
    position: absolute;
    top: 112px;
    left: 0;
    right: 0;
    margin: 0;
    font-family: "Archivo Black", sans-serif;
    font-variant: small-caps;
    font-weight: 400;
    font-size: 36px;
    letter-spacing: 0.5px;
    color: var(--ink);
  }
  .person {
    position: absolute;
    top: 222px;
    left: 0;
    right: 0;
    font-family: "Arimo", sans-serif;
  }
  .person-name {
    margin: 0;
    font-size: 32px;
    font-weight: 400;
    line-height: 1;
  }
  .person-role {
    margin: 2px 0 0;
    font-size: 19px;
    line-height: 1;
  }
  .address {
    position: absolute;
    top: 430px;
    left: 0;
    right: 0;
    font-family: "Arimo", sans-serif;
    font-style: normal;
    font-size: 23px;
    line-height: 1.2;
  }
  .home-icon {
    display: block;
    width: 30px;
    height: 26px;
    margin: 0 auto 8px;
    fill: var(--accent);
  }
  .swoosh {
    position: absolute;
    left: 0;
    bottom: 0;
    width: 446px;
    height: 780px;
  }
  .swoosh .edge { fill: var(--accent); }
  .swoosh .base { fill: var(--ink); }
</style>
</head>
<body>
<main class="canvas">
  <article class="business-card">
    <h1 class="brand-name">Copper Gate BBQ</h1>

    <div class="person">
      <p class="person-name">Walt Barcombe</p>
      <p class="person-role">Owner</p>
    </div>

    <address class="address">
      <svg class="home-icon" viewBox="0 0 30 26" aria-hidden="true">
        <path d="M15 1 L1 13 H5 V25 H12 V17 H18 V25 H25 V13 H29 Z"/>
        <rect x="21" y="3" width="3" height="6"/>
      </svg>
      2218 Dunmore Ave. Millbrook,<br>In. 46391
    </address>

    <svg class="swoosh" viewBox="0 0 446 780" aria-hidden="true">
      <path class="edge" d="M0 715 C110 690 190 628 290 602 C350 588 410 582 446 584 L446 780 L0 780 Z"/>
      <path class="base" d="M0 726 C115 700 200 642 300 618 C360 604 412 600 446 602 L446 780 L0 780 Z"/>
    </svg>
  </article>
</main>
</body>
</html>
```